design a construction company business card

Design business card around our logo. Card must have all the typical info: name, title, address, phone, email, business name, etc. Somewhere on the card I would like to see our motto "Solid Foundations... Driven by Lasting Quality." Consider adding a splash of bright orange to the card to complement the blues and silvers/grays in the logo. We are open to metallic inks, textures, etc. We would like to see options on both light and dark backgrounds. The font in the logo is Euro Technic Extended Regular.

```html
<!DOCTYPE html>
<html lang="en">
<head>
<meta charset="utf-8">
<title>Halden Contracting – Business Card</title>
<link href="https://fonts.googleapis.com/css2?family=Roboto:wght@400;500;700&display=swap" rel="stylesheet">
<style>
  :root {
    --backdrop: #f7f7f7;
    --navy: #0e1730;
    --silver: #85868a;
    --white: #ffffff;
    --blue: #1f63b8;
    --text-grey: #6b6d72;
    --motto-grey: #8e929b;
  }
  * { margin: 0; padding: 0; box-sizing: border-box; }
  html, body {
    width: 1200px; height: 1000px; overflow: hidden;
    background: var(--backdrop);
    font-family: "Roboto", Arial, sans-serif;
  }
  .card {
    position: absolute;
    box-shadow: 0 14px 22px rgba(0,0,0,0.28);
    overflow: hidden;
  }
  .card svg.card-bg { position: absolute; inset: 0; }
  .card-front { left: 255px; top: 72px; width: 689px; height: 394px; background: var(--navy); }
  .card-back { left: 251px; top: 529px; width: 698px; height: 399px; background: var(--white); }

  .wordmark {
    position: absolute;
    color: var(--blue);
    font-weight: 500;
    letter-spacing: 1px;
    white-space: nowrap;
  }
  .card-front .wordmark {
    left: 0; width: 100%; top: 205px; text-align: center;
    font-size: 30px; color: #2d73cf;
  }
  .motto {
    position: absolute; left: 0; width: 100%; top: 284px;
    text-align: center; font-size: 17px; color: var(--motto-grey);
    letter-spacing: 0.3px;
  }
  .card-back .wordmark { right: 48px; top: 120px; font-size: 22px; }

  .holder-name {
    position: absolute; right: 48px; top: 186px;
    font-size: 26px; font-weight: 500; color: var(--blue);
  }
  .holder-title {
    position: absolute; right: 48px; top: 220px;
    font-size: 17px; color: var(--text-grey);
  }
  .holder-title .company { color: var(--blue); font-weight: 500; }
  .divider {
    position: absolute; left: 42px; top: 228px; width: 342px; height: 2px;
    background: var(--blue);
  }
  .contact-list { position: absolute; left: 34px; top: 248px; list-style: none; }
  .contact-list li {
    display: flex; align-items: center; height: 28px;
    font-size: 17px; color: var(--text-grey);
  }
  .contact-list svg { width: 20px; height: 20px; margin-right: 8px; fill: var(--blue); }
  .address {
    position: absolute; right: 48px; top: 307px;
    text-align: right; font-size: 17px; line-height: 26px; color: var(--text-grey);
    font-style: normal;
  }
</style>
</head>
<body>

<section class="card card-front">
  <svg class="card-bg" width="689" height="394" viewBox="0 0 689 394">
    <path d="M0 0 H222 C130 40 50 110 0 190 Z" fill="var(--silver)"/>
    <path d="M613 394 C650 370 675 350 689 328 V394 Z" fill="var(--silver)"/>
  </svg>
  <div class="wordmark">HALDEN CONTRACTING, INC.</div>
  <p class="motto">Solid Foundations... Driven by Lasting Quality</p>
</section>

<section class="card card-back">
  <svg class="card-bg" width="698" height="399" viewBox="0 0 698 399">
    <path d="M0 0 H227 C130 40 45 110 0 191 Z" fill="var(--silver)"/>
    <path d="M621 399 C655 380 685 355 698 331 V399 Z" fill="var(--silver)"/>
  </svg>
  <div class="wordmark">HALDEN CONTRACTING, INC.</div>

  <h1 class="holder-name">Mark Ellison</h1>
  <p class="holder-title">CEO of <span class="company">Halden Contracting, INC</span></p>
  <div class="divider"></div>

  <ul class="contact-list">
    <li>
      <svg viewBox="0 0 24 24"><path d="M6.6 10.8a15 15 0 0 0 6.6 6.6l2.2-2.2a1 1 0 0 1 1-.25 11.4 11.4 0 0 0 3.6.57 1 1 0 0 1 1 1V20a1 1 0 0 1-1 1A17 17 0 0 1 3 4a1 1 0 0 1 1-1h3.5a1 1 0 0 1 1 1c0 1.25.2 2.450.57 3.57a1 1 0 0 1-.25 1z"/></svg>
      (02) 9550 1234
    </li>
    <li>
      <svg viewBox="0 0 24 24"><path d="M7 1h10a2 2 0 0 1 2 2v18a2 2 0 0 1-2 2H7a2 2 0 0 1-2-2V3a2 2 0 0 1 2-2zm0 3v14h10V4zm5 15.2a1.2 1.2 0 1 0 0 2.4 1.2 1.2 0 0 0 0-2.4z"/></svg>
      0400 123 456
    </li>
    <li>
      <svg viewBox="0 0 24 24"><path d="M2 5h20v14H2zm2 2v.5l8 5 8-5V7z"/></svg>
      info@haldencontracting.com
    </li>
    <li>
      <svg viewBox="0 0 24 24"><path d="M12 2a10 10 0 1 0 0 20 10 10 0 0 0 0-20zm-1 17.9A8 8 0 0 1 4.1 10.9L9 16v1a2 2 0 0 0 2 2zm6.9-2.5A2 2 0 0 0 16 16h-1v-3a1 1 0 0 0-1-1H8v-2h2a1 1 0 0 0 1-1V7h2a2 2 0 0 0 2-2v-.4a8 8 0 0 1 2.9 12.8z"/></svg>
      www.haldencontracting.com
    </li>
  </ul>

  <address class="address">
    18 Carter Lane, Ryde<br>NSW 2112, NY
  </address>
</section>

</body>
</html>
```